Flyer Design Project

Need a DL Size flyer (2 sided) for letter box marketing for our website www.brightwardsecure.com.au
Updates

Project Deadline Extended
Reason: Thank you for submitting the designs. We like few of the designs and will request those designers to changes few things to make it more suitable for us. Because of holidays need to extend the deadlines. Thank you.

Industry/Entity Type

Marketing

```html
<!DOCTYPE html>
<html lang="en">
<head>
<meta charset="utf-8">
<title>Brightward CCTV – DL Flyer, Both Sides</title>
<link rel="stylesheet" href="https://fonts.googleapis.com/css2?family=Arimo:wght@400;700&display=swap">
<style>
  :root {
    --page: #ffffff;
    --navy: #0a1f5c;
    --royal: #1846a8;
    --sky: #3f86d8;
    --glow: #9fd0ff;
    --brand-yellow: #f6c21c;
    --white: #ffffff;
    --ink: #0d1a3a;
    --card: rgba(200, 220, 250, 0.55);
    --card-lit: rgba(230, 240, 255, 0.85);
    --price: #2b3f9e;
    --price-text: #ffe14d;
    --purple: #7d3a9a;
    --purple-soft: #b77ed0;
    --green: #2f9a3a;
    --green-soft: #5cc24f;
    --red: #c02030;
    --red-soft: #e0566a;
    --label: #111111;
  }
  * { box-sizing: border-box; margin: 0; padding: 0; }
  html, body { width: 1200px; height: 724px; overflow: hidden; background: var(--page); }
  body { position: relative; font-family: "Arimo", Arial, sans-serif; color: var(--white); }

  .flyer {
    position: absolute; top: 11px; height: 643px; overflow: hidden;
    border: 1px solid #333;
  }
  .flyer--front { left: 24px; width: 473px;
    background: radial-gradient(ellipse at 50% 45%, var(--glow) 0%, var(--sky) 30%, var(--royal) 65%, var(--navy) 100%); }
  .flyer--back { left: 667px; width: 504px;
    background: linear-gradient(160deg, var(--royal) 0%, #1a3b94 45%, var(--navy) 100%); }

  .masthead {
    position: absolute; left: 0; top: 0; right: 0; height: 93px;
    background: linear-gradient(180deg, #1a2d6e 0%, var(--navy) 100%);
    border-bottom: 1px solid rgba(255,255,255,0.25);
  }
  .masthead__mark {
    position: absolute; left: 96px; top: 16px; width: 40px; height: 40px;
    border-radius: 50%; background: #cfd6e2;
  }
  .masthead__name {
    position: absolute; left: 148px; top: 12px;
    font-weight: 700; font-size: 36px; line-height: 1; color: var(--brand-yellow);
    white-space: nowrap;
  }
  .masthead__tagline {
    position: absolute; left: 160px; top: 56px;
    font-weight: 700; font-size: 20px; line-height: 1; color: var(--white);
  }
  .flyer--back .masthead__mark { left: 112px; }
  .flyer--back .masthead__name { left: 164px; }
  .flyer--back .masthead__tagline { left: 176px; }

  /* Front: package grid */
  .package {
    position: absolute; width: 139px; padding: 5px 5px 6px;
    background: var(--card); text-align: center; color: var(--ink);
  }
  .package--lit { background: var(--card-lit); }
  .package__title { font-weight: 700; font-size: 8px; line-height: 10px; color: var(--navy); }
  .package__media {
    display: block; margin: 4px auto 5px; width: 118px; height: 62px;
    background: linear-gradient(180deg, #d9dee8 0%, #8a95a8 100%);
  }
  .package__specs { list-style: none; font-size: 6.2px; line-height: 8.2px; }
  .package__price {
    margin: 6px auto 0; width: 100px; padding: 3px 0;
    background: var(--price); color: var(--price-text);
    font-weight: 700; font-size: 11px; line-height: 12px;
  }

  /* Back: offers */
  .offer { position: absolute; left: 0; width: 504px; }
  .offer__media {
    position: absolute; left: 22px; width: 180px;
  }
  .offer__caption {
    position: absolute; left: 22px; width: 180px;
    font-weight: 700; font-size: 7px; color: var(--white);
  }
  .offer__heading {
    position: absolute; left: 207px; width: 267px; height: 30px;
    font-weight: 700; font-size: 17px; line-height: 30px; text-align: center; color: var(--white);
  }
  .offer__sub {
    position: absolute; left: 207px; width: 267px; height: 13px;
    font-weight: 700; font-size: 9.5px; line-height: 13px; text-align: center; color: var(--white);
  }
  .offer__list { position: absolute; left: 232px; width: 242px; list-style: none; }
  .offer__list li {
    position: relative; font-size: 9.5px; line-height: 15px; color: #e8eeff;
  }
  .offer__list li::after {
    content: ""; position: absolute; right: 0; top: 2px; width: 16px; height: 11px;
    background: var(--swatch);
  }
  .offer__price {
    position: absolute; left: 232px; width: 242px; height: 17px;
    font-weight: 700; font-size: 11px; line-height: 17px; text-align: center; color: var(--white);
  }
  .offer--purple { --tone: var(--purple); --soft: var(--purple-soft); --swatch: var(--purple-soft); }
  .offer--green { --tone: var(--green); --soft: var(--green-soft); --swatch: var(--green-soft); }
  .offer--red { --tone: var(--red); --soft: var(--red-soft); --swatch: var(--red-soft); }
  .offer__heading { background: var(--tone); }
  .offer__sub { background: var(--soft); }
  .offer__price { background: var(--tone); }
  .divider { position: absolute; left: 22px; width: 460px; height: 2px; background: var(--white); }

  .side-label {
    position: absolute; top: 668px; width: 200px; text-align: center;
    font-weight: 700; font-size: 27px; color: var(--label);
  }
</style>
</head>
<body>

<section class="flyer flyer--front" aria-label="Flyer side one">
  <header class="masthead">
    <span class="masthead__mark"></span>
    <span class="masthead__name">Brightward CCTV</span>
    <span class="masthead__tagline">CCTV System Specialist</span>
  </header>

  <article class="package" style="left:22px; top:118px;">
    <h3 class="package__title">Package 1<br>Standalone DVR System (2 Cameras)</h3>
    <span class="package__media" role="img" aria-label="Photo of DVR, monitor and two dome cameras"></span>
    <ul class="package__specs">
      <li>2 X high resolution dome cameras</li><li>1 X 4 channel standalone DVR</li>
      <li>500GB hard drive</li><li>19" LCD monitor</li>
      <li>Remote access from PCs &amp; Phones*</li><li>Easy to use</li>
      <li>1 Year Warranty</li><li>Full system supplied &amp; installed</li>
    </ul>
    <p class="package__price">$1495<br>+ GST*</p>
  </article>

  <article class="package package--lit" style="left:167px; top:110px;">
    <h3 class="package__title">Package 2<br>Standalone DVR System (4 Cameras)</h3>
    <span class="package__media" role="img" aria-label="Photo of DVR, monitor and four dome cameras"></span>
    <ul class="package__specs">
      <li>4 X high resolution dome cameras</li><li>1 X 4 channel standalone DVR</li>
      <li>500GB hard drive</li><li>19" LCD monitor</li>
      <li>Remote access from PCs &amp; Phones*</li><li>Easy to use</li>
      <li>1 Year Warranty</li><li>Full system supplied &amp; installed</li>
    </ul>
    <p class="package__price">$2195<br>+ GST*</p>
  </article>

  <article class="package" style="left:312px; top:118px;">
    <h3 class="package__title">Package 3<br>Standalone DVR System (8 Cameras)</h3>
    <span class="package__media" role="img" aria-label="Photo of DVR, monitor and eight dome cameras"></span>
    <ul class="package__specs">
      <li>8 X high resolution dome cameras</li><li>1 X 8 channel standalone DVR</li>
      <li>1 Terabyte hard drive</li><li>19" LCD monitor</li>
      <li>Remote access from PCs &amp; Phones*</li><li>Easy to use</li>
      <li>1 Year Warranty</li><li>Full system supplied &amp; installed</li>
    </ul>
    <p class="package__price">$3295<br>+ GST*</p>
  </article>

  <article class="package" style="left:22px; top:372px;">
    <h3 class="package__title">Package 4<br>IP based CCTV System (2 Cameras)</h3>
    <span class="package__media" role="img" aria-label="Photo of NVR, monitor and two IP cameras"></span>
    <ul class="package__specs">
      <li>2 X 2 Megapixel IP Cameras</li><li>1 X PC based NVR System</li>
      <li>500GB hard drive</li><li>19" LCD Monitor</li>
      <li>Remote Access from PCs and Phones*</li><li>Easy to use</li>
      <li>1 Year warranty</li><li>Full system supplied &amp; installed</li>
    </ul>
    <p class="package__price">$1995<br>+ GST*</p>
  </article>

  <article class="package package--lit" style="left:167px; top:364px; padding-bottom:18px;">
    <h3 class="package__title">Package 5<br>IP based CCTV System (4 Cameras)</h3>
    <span class="package__media" role="img" aria-label="Photo of NVR, monitor and four IP cameras"></span>
    <ul class="package__specs">
      <li>4 X 2 Megapixel IP Cameras</li><li>1 X PC based NVR System</li>
      <li>1 Terabyte hard drive</li><li>19" LCD Monitor</li>
      <li>Remote Access from PCs and Phones*</li><li>Easy to use</li>
      <li>1 Year warranty</li><li>Full system supplied &amp; installed</li>
    </ul>
    <p class="package__price">$3295<br>+ GST*</p>
  </article>

  <article class="package" style="left:312px; top:372px;">
    <h3 class="package__title">Package 6<br>IP based CCTV System (8 Cameras)</h3>
    <span class="package__media" role="img" aria-label="Photo of NVR, monitor and eight IP cameras"></span>
    <ul class="package__specs">
      <li>8 X 2 Megapixel IP Cameras</li><li>1 X PC based NVR System</li>
      <li>2 Terabyte hard drive</li><li>19" LCD Monitor</li>
      <li>Remote Access from PCs and Phones*</li><li>Easy to use</li>
      <li>1 Year warranty</li><li>Full system supplied &amp; installed</li>
    </ul>
    <p class="package__price">$4495<br>+ GST*</p>
  </article>
</section>

<section class="flyer flyer--back" aria-label="Flyer side two">
  <header class="masthead">
    <span class="masthead__mark"></span>
    <span class="masthead__name">Brightward CCTV</span>
    <span class="masthead__tagline">CCTV System Specialist</span>
  </header>

  <article class="offer offer--purple" style="top:0;">
    <span class="offer__media" style="top:112px; height:132px; background:radial-gradient(circle at 50% 45%, #f2f2f2 0%, #b8bec8 55%, rgba(40,70,150,0) 75%);" role="img" aria-label="Photo of a high resolution dome camera"></span>
    <p class="offer__caption" style="top:252px;">High Resolution Cameras &amp; DVRs</p>
    <h3 class="offer__heading" style="top:117px;">CCTV System Package 1</h3>
    <p class="offer__sub" style="top:147px;">Standalone DVR System (2 Cameras)</p>
    <ul class="offer__list" style="top:168px;">
      <li>- 1 X 4 Channel standalone DVR</li>
      <li>- Full system supplied &amp; installed</li>
      <li>- 2 X High resolution dome cameras</li>
      <li>- 1 Year full hardware warranty*</li>
    </ul>
    <p class="offer__price" style="top:234px;">$1495 + GST</p>
  </article>

  <span class="divider" style="top:282px;"></span>

  <article class="offer offer--green" style="top:0;">
    <span class="offer__media" style="top:300px; height:130px; background:linear-gradient(135deg, #6b4a2a 0%, #3a5f8a 50%, #1c1c1c 100%);" role="img" aria-label="Photo of smart phones showing live camera views"></span>
    <p class="offer__caption" style="top:436px;">Remote Access from Smart Phones</p>
    <h3 class="offer__heading" style="top:300px;">CCTV System Package 2</h3>
    <p class="offer__sub" style="top:330px;">Standalone DVR System (4 Cameras)</p>
    <ul class="offer__list" style="top:351px;">
      <li>- 1 X 4 Channel standalone DVR</li>
      <li>- Full system supplied &amp; installed</li>
      <li>- 4 X High resolution dome cameras</li>
      <li>- 1 Year full hardware warranty*</li>
    </ul>
    <p class="offer__price" style="top:417px;">$1495 + GST</p>
  </article>

  <span class="divider" style="top:465px;"></span>

  <article class="offer offer--red" style="top:0;">
    <span class="offer__media" style="top:482px; height:125px; background:linear-gradient(180deg, #3c3c3c 0%, #7a6a55 50%, #1a1a1a 100%);" role="img" aria-label="Photo of a monitor showing four camera recordings"></span>
    <p class="offer__caption" style="top:614px;">Motion Detection or 24x7 Recordings</p>
    <h3 class="offer__heading" style="top:481px;">CCTV System Package 3</h3>
    <p class="offer__sub" style="top:511px;">Standalone DVR System (8 Cameras)</p>
    <ul class="offer__list" style="top:532px;">
      <li>- 1 X 4 Channel standalone DVR</li>
      <li>- Full system supplied &amp; installed</li>
      <li>- 4 X High resolution dome cameras</li>
      <li>- 1 Year full hardware warranty*</li>
    </ul>
    <p class="offer__price" style="top:598px;">$1495 + GST</p>
  </article>
</section>

<p class="side-label" style="left:161px;">1-side</p>
<p class="side-label" style="left:819px;">2-side</p>

</body>
</html>
```